Lanterns Over the Silent Harbor

This book cover must convey the fact that the scientific evidence is clear that the afterlife is a reality. Attached are two ideas, but they're not working for me as they are. It could be that I'm not a graphic artist and can't get the composition correct. If there is a view of the afterlife, it must be realistic. The afterlife is just like this life. We can't use the family photo. I don't have permission.

```html
<!DOCTYPE html>
<html lang="en">
<head>
<meta charset="utf-8">
<title>Lanterns Over the Silent Harbor – Book Cover</title>
<link rel="stylesheet" href="https://fonts.googleapis.com/css2?family=Cinzel:wght@400;500&family=Vollkorn:wght@500&display=swap">
<style>
  :root {
    --backdrop: #8a8a8a;
    --sky-top: #4f8fcb;
    --sky-mid: #8fbde4;
    --sky-glow: #f4f9fd;
    --sea: #3fa3b4;
    --foam: #eef3f5;
    --sand: #d9cbb8;
    --title-navy: #12306f;
    --title-red: #e0202b;
    --author-ink: #1a1a1a;
  }
  * { margin: 0; padding: 0; box-sizing: border-box; }
  html, body {
    width: 1200px;
    height: 800px;
    overflow: hidden;
    background: var(--backdrop);
  }
  .canvas {
    position: relative;
    width: 1200px;
    height: 800px;
  }
  .cover {
    position: absolute;
    left: 384px;
    top: 40px;
    width: 432px;
    height: 720px;
    overflow: hidden;
  }
  .cover-art {
    position: absolute;
    inset: 0;
    background:
      radial-gradient(circle at 46% 48%, var(--sky-glow) 0, rgba(244,249,253,0.85) 12%, rgba(244,249,253,0) 42%),
      linear-gradient(to bottom,
        var(--sky-top) 0%,
        var(--sky-mid) 35%,
        #cfe3f2 62%,
        #dbe9f3 69%,
        var(--sea) 72%,
        #8fc3cc 77%,
        var(--foam) 82%,
        #e7e3db 92%,
        var(--sand) 100%);
  }
  .rays {
    position: absolute;
    inset: 0;
    width: 100%;
    height: 100%;
  }
  .title {
    position: absolute;
    left: 0;
    right: 0;
    top: 112px;
    font-family: "Cinzel", serif;
    font-weight: 500;
    color: var(--title-navy);
    line-height: 1;
  }
  .title-line {
    display: block;
    white-space: nowrap;
  }
  .title-main {
    font-size: 56px;
    letter-spacing: -1px;
  }
  .title-main .initial {
    font-size: 82px;
  }
  .title-lead { padding-left: 34px; }
  .title-link {
    font-size: 30px;
    color: var(--title-red);
    font-weight: 400;
    padding-left: 82px;
    margin-top: 12px;
    letter-spacing: 0.5px;
  }
  .title-close {
    padding-left: 34px;
    margin-top: -6px;
  }
  .author {
    position: absolute;
    left: 0;
    right: 0;
    bottom: 44px;
    text-align: center;
    font-family: "Vollkorn", serif;
    font-weight: 500;
    font-size: 22px;
    color: var(--author-ink);
    letter-spacing: 0.5px;
  }
</style>
</head>
<body>
<main class="canvas">
  <article class="cover">
    <div class="cover-art" role="img" aria-label="Bright sky with sun rays and clouds over the sea, waves breaking on a sandy beach with a family holding hands at the shoreline"></div>
    <svg class="rays" viewBox="0 0 432 720" aria-hidden="true">
      <g stroke="#ffffff" stroke-opacity="0.45" stroke-width="1">
        <line x1="198" y1="345" x2="20" y2="0"/>
        <line x1="198" y1="345" x2="70" y2="0"/>
        <line x1="198" y1="345" x2="130" y2="0"/>
        <line x1="198" y1="345" x2="190" y2="0"/>
        <line x1="198" y1="345" x2="250" y2="0"/>
        <line x1="198" y1="345" x2="310" y2="0"/>
        <line x1="198" y1="345" x2="380" y2="0"/>
        <line x1="198" y1="345" x2="432" y2="40"/>
        <line x1="198" y1="345" x2="0" y2="70"/>
      </g>
    </svg>
    <h1 class="title">
      <span class="title-line title-main title-lead"><span class="initial">L</span>ANTERNS</span>
      <span class="title-line title-link">OVER THE SILENT</span>
      <span class="title-line title-main title-close"><span class="initial">H</span>ARBOR</span>
    </h1>
    <p class="author">R. Elliot Marsh, PhD</p>
  </article>
</main>
</body>
</html>
```